Cardiologist needs a unique and unforgettable business card design

Hi, I am a Cardiologist (heart specialist) and I need a business card as I am starting out my own practice very soon.
I have so used to seeing very boring and forgettable business cards that people take one look and then it goes into the bin.
I hope you can design one card that tells people immediately that it is from a Cardiologist (Heart Specialist) who is good, experienced, mature and save lives.
My colours that I like are green/white/earthly tones but I am also open to various colours combinations.
My clinic name is called Velmar Cardiology and I am attaching the Logo and information needed on the name card for you.
I would like the definition of Velmar to be in the name card
Velmar - To save one suffering from disease, to make well, heal, preserve,
restore to health and to make whole one again
I would like to have Spot UV or Embossing or Both to make the card stand out.
Thank you very much

```html
<!DOCTYPE html>
<html lang="en">
<head>
<meta charset="utf-8">
<title>Velmar Cardiology – Business Card</title>
<link rel="stylesheet" href="https://fonts.googleapis.com/css2?family=Roboto+Condensed:wght@400;700&family=Cormorant+Garamond:wght@400&display=swap">
<style>
  :root {
    --page-bg: #2b2b2b;
    --card-green: #52ab2a;
    --card-green-light: #5cb632;
    --card-green-dark: #479a23;
    --ink-white: #ffffff;
    --accent-red: #c8202c;
  }
  * { margin: 0; padding: 0; box-sizing: border-box; }
  html, body {
    width: 1200px;
    height: 900px;
    overflow: hidden;
    background: var(--page-bg);
  }
  .business-card {
    position: absolute;
    left: 100px;
    top: 165px;
    width: 1000px;
    height: 570px;
    border-radius: 34px;
    background: linear-gradient(135deg, var(--card-green-light) 0%, var(--card-green) 50%, var(--card-green-dark) 100%);
    color: var(--ink-white);
    overflow: hidden;
  }
  .definition {
    position: absolute;
    right: 70px;
    top: 120px;
    width: 560px;
    text-align: right;
    font-family: "Roboto Condensed", sans-serif;
    font-weight: 400;
    font-size: 22px;
    line-height: 1.3;
  }
  .definition-term {
    display: block;
    font-weight: 700;
    font-size: 21px;
    margin-bottom: 2px;
  }
  .brand {
    position: absolute;
    left: 80px;
    top: 270px;
  }
  .brand-name {
    display: flex;
    align-items: center;
    gap: 22px;
    font-family: "Roboto Condensed", sans-serif;
    font-weight: 400;
    font-size: 70px;
    letter-spacing: 2px;
    line-height: 1;
  }
  .brand-dot {
    width: 34px;
    height: 34px;
    border-radius: 50%;
    background: var(--accent-red);
    flex-shrink: 0;
  }
  .tagline {
    margin-top: 18px;
    margin-left: 58px;
    font-family: "Cormorant Garamond", serif;
    font-size: 27px;
    letter-spacing: 5px;
  }
</style>
</head>
<body>
  <div class="business-card">
    <p class="definition">
      To save one suffering from disease, to make well, heal, preserve, restore to health and to make whole one again
      <span class="definition-term">VELMAR</span>
    </p>
    <div class="brand">
      <div class="brand-name">
        <span class="brand-dot"></span>
        <span>Velmar Cardiology</span>
      </div>
      <p class="tagline">Saving hearts • Saving lives</p>
    </div>
  </div>
</body>
</html>
```